Redesign of key pages of website

We have a website in development: (You can see the test version here: https://staging.pipwoof.ai) We want a redesign of a) the home page, b) the set up screens (all four steps), c) the account home page, and the chat page (all four linked below). It needs to look amazing in both desktop and mobile. Also, the chat page needs to have a few different versions to give people a choice between them.

Four areas:
1) Home page: https://staging.pipwoof.ai/
2) Account pages: https://staging.pipwoof.ai/account/chatsettings.php?step=1
3) Account home page (you'll need to set up an account which is free): https://staging.pipwoof.ai/account/summary.php
4) Chat page: https://staging.pipwoof.ai/chat.php?id=375

Also to clarify re: code, I don't need any of the interaction/behavior code. I just need the basic HTML and stylesheets so I can integrate that into the existing website.

Please feel free to pass by early versions to me or if you have any clarifications, let me know!

Industry/Entity Type

small businesses

Coding

Coded - Design and coding required

Number of Pages Required

5+ page

Font styles to use
Other font styles liked:
• keep the current font.

Requirements
Must have
• All the same elements/functionality on the current site. Just want a redesign. Also keep the dog visual. Also must work great in mobile and desktop and be really fun and modern and easy.
Nice to have
• Also in the setup pages, need a much better form of navigation (currently just have four circles.)

```html
<!DOCTYPE html>
<html lang="en">
<head>
<meta charset="utf-8">
<title>Pipwoof – Chat with my AI assistant</title>
<link href="https://fonts.googleapis.com/css2?family=Raleway:wght@700;800&family=Poppins:wght@300;400;500;600&family=Open+Sans:wght@400&display=swap" rel="stylesheet">
<style>
  :root{
    --page-bg:#eef4fd;
    --blue-deep:#2677e6;
    --blue:#3f8bf8;
    --blue-soft:#7aacf8;
    --blue-text:#3d86f0;
    --ink:#2a2f3a;
    --muted:#c9cdd5;
    --white:#ffffff;
    --pup-light:#c9d2fb;
  }
  *{box-sizing:border-box;margin:0;padding:0}
  html,body{width:1200px;height:1127px;overflow:hidden}
  body{position:relative;background:var(--page-bg);font-family:"Poppins",sans-serif;color:var(--ink)}
  .backdrop{position:absolute;inset:0;width:1200px;height:1127px}
  .site-header{position:absolute;top:0;left:0;width:1200px;height:70px}
  .brand{position:absolute;left:162px;top:20px;display:flex;align-items:center;gap:10px;font-family:"Poppins",sans-serif;font-weight:600;font-size:28px;line-height:36px;color:var(--white)}
  .brand-dot{width:14px;height:14px;border-radius:50%;background:var(--white)}
  .main-nav{position:absolute;left:584px;top:31px;display:flex;gap:28px}
  .main-nav a{font-family:"Raleway",sans-serif;font-weight:700;font-size:10.5px;color:var(--white);text-decoration:none}
  .login-btn{position:absolute;left:926px;top:22px;width:111px;height:32px;background:var(--white);border-radius:6px;display:flex;align-items:center;justify-content:center;gap:6px;font-size:8.5px;font-weight:500;color:var(--ink);text-decoration:none}
  .hero-title{position:absolute;left:167px;top:150px;font-family:"Raleway",sans-serif;font-weight:700;font-size:37px;color:var(--white)}
  .mascot{position:absolute;left:694px;top:80px;width:250px;height:250px;border-radius:46% 46% 40% 40%;background:radial-gradient(circle at 55% 40%,var(--pup-light) 0 45%,var(--blue) 75%)}
  .card{position:absolute;top:435px;height:367px;background:var(--white);border-radius:6px}
  .profile-card{left:162px;width:272px;text-align:center}
  .avatar{position:absolute;left:61px;top:-49px;width:152px;height:152px;border-radius:50%;background:linear-gradient(160deg,#c8c4bd,#b98f5e 50%,#6e7a5a);border:5px solid #eef3fd}
  .profile-name{position:absolute;left:0;right:0;top:115px;font-family:"Raleway",sans-serif;font-weight:800;font-size:31px;color:var(--blue-text)}
  .profile-role{position:absolute;left:0;right:0;top:155px;font-family:"Open Sans",sans-serif;font-size:12.5px}
  .profile-pitch{position:absolute;left:0;right:0;top:185px;font-size:21px;font-weight:300;line-height:31px;color:#222}
  .link-btn{position:absolute;left:61px;width:151px;height:40px;background:var(--white);border-radius:9px;box-shadow:0 6px 14px rgba(60,90,150,.14);display:flex;align-items:center;justify-content:center;gap:10px;font-size:11px;font-weight:500;color:var(--ink);text-decoration:none}
  .link-btn.home{top:252px}
  .link-btn.demo{top:308px}
  .chat-card{left:456px;width:581px}
  .chat-greeting{position:absolute;left:48px;top:28px;font-size:12.5px;color:#333}
  .chat-input{position:absolute;left:330px;top:78px;width:200px;border:0;outline:0;background:none;font-family:"Poppins",sans-serif;font-size:12.5px;color:var(--muted)}
  .chat-input::placeholder{color:var(--muted);opacity:1}
  .site-footer{position:absolute;left:162px;right:161px;top:1061px;display:flex;justify-content:space-between;font-size:12.5px;color:var(--white)}
  .site-footer a{color:var(--white)}
</style>
</head>
<body>
  <svg class="backdrop" viewBox="0 0 1200 1127" aria-hidden="true">
    <path d="M0 330 Q40 360 0 820 Z" fill="#e2ecfb"/>
    <path d="M0 0 H1200 V150 C1120 200 1020 230 890 212 C760 195 690 200 600 250 C470 330 330 370 200 345 C110 328 40 260 0 230 Z" fill="var(--blue-soft)"/>
    <path d="M0 0 H1200 V150 C1130 205 1030 225 920 215 C800 200 730 185 640 210 C520 245 450 330 330 325 C200 320 80 260 0 188 Z" fill="var(--blue-deep)"/>
    <path d="M0 0 H420 C380 60 280 90 180 80 C110 72 50 50 0 35 Z" fill="var(--blue)" opacity=".7"/>
    <path d="M0 875 C90 945 200 975 330 972 C560 965 730 880 860 840 C960 810 1080 840 1200 866 V1127 H0 Z" fill="var(--blue)"/>
  </svg>

  <header class="site-header">
    <div class="brand"><span class="brand-dot"></span>Pipwoof</div>
    <nav class="main-nav">
      <a href="https://staging.pipwoof.ai/">HOME</a>
      <a href="https://staging.pipwoof.ai/account/chatsettings.php?step=1">ACCOUNT</a>
      <a href="https://staging.pipwoof.ai/account/summary.php">ACCOUNT HOME</a>
      <a href="https://staging.pipwoof.ai/chat.php?id=375">CHAT</a>
    </nav>
    <a class="login-btn" href="#">Login or Register
      <svg width="15" height="8" viewBox="0 0 15 8"><path d="M0 4H13M10 1L13.5 4L10 7" fill="none" stroke="#3d86f0" stroke-width="1.3"/></svg>
    </a>
  </header>

  <h1 class="hero-title">Chat with my AI assistant.</h1>
  <div class="mascot" role="img" aria-label="Friendly blue cartoon puppy mascot"></div>

  <section class="card profile-card">
    <div class="avatar" role="img" aria-label="Portrait photo of Nora, hair stylist"></div>
    <h2 class="profile-name">NORA</h2>
    <p class="profile-role">Hair Stylist</p>
    <p class="profile-pitch">Talk to Pip, my<br>AI assistant.</p>
    <a class="link-btn home" href="#">My home page
      <svg width="19" height="10" viewBox="0 0 19 10"><path d="M0 5H17M13 1L17.5 5L13 9" fill="none" stroke="#3d86f0" stroke-width="1.6"/></svg>
    </a>
    <a class="link-btn demo" href="#">Another demo link
      <svg width="19" height="10" viewBox="0 0 19 10"><path d="M0 5H17M13 1L17.5 5L13 9" fill="none" stroke="#3d86f0" stroke-width="1.6"/></svg>
    </a>
  </section>

  <section class="card chat-card">
    <p class="chat-greeting">Hi. I'm Nora's AI assistant. What's your name?</p>
    <input class="chat-input" type="text" placeholder="Type your response.....">
  </section>

  <footer class="site-footer">
    <span>© 2023 Pipwoof.ai. All rights reserved. <a href="#">Terms of Use</a></span>
    <span>Have feedback? <a href="#">Let us know!</a></span>
  </footer>
</body>
</html>
```